Management Consulting needing a cool business card for client acquisition and networking

We are looking for a business card that is progressive and fresh that conveys innovation, forward thinking, and confidence. The business card is for a company based in Charlotte NC called, 'MERIDOX CONSULTING GROUP LLC'. The company primarily works with banks, insurance, and brokerages to implement innovative solutions to help them streamline their operations, to more effectively manage risks, and to improve their customer relationships.

Target Market(s)

Typically meet with Chief Financial Officers, Chief Information Officers, Chief Operations Officer, Business Unit Leader. The target market are generally 40-55 years, male, white, master level education plus.

Industry/Entity Type

Progressive

Font styles to use
Serif
Other font styles liked:
• Calibri

Requirements
Should not have
• Designs that look too much like law firms or accounting companies. Too conservative

```html
<!DOCTYPE html>
<html lang="en">
<head>
<meta charset="utf-8">
<title>Meridox Consulting Group LLC – Business Card</title>
<link href="https://fonts.googleapis.com/css2?family=Open+Sans:wght@400;600;700&display=swap" rel="stylesheet">
<style>
  :root {
    --backdrop: #d9d9d9;
    --card: #f4f5f4;
    --ink: #5a5a5a;
    --ink-soft: #8a8a8a;
    --accent: #c6202a;
    --ring: #d0d0d0;
    --ring-faint: #e4e2e0;
  }
  * { margin: 0; padding: 0; box-sizing: border-box; }
  html, body {
    width: 1200px; height: 900px; overflow: hidden;
    background: var(--backdrop);
    font-family: "Open Sans", Calibri, Arial, sans-serif;
  }
  .canvas {
    position: relative; width: 1200px; height: 900px;
  }
  .card {
    position: absolute; left: 250px; width: 700px; height: 400px;
    background: var(--card);
    box-shadow: 0 6px 18px rgba(0,0,0,0.18);
    overflow: hidden;
  }
  .card--front { top: 35px; }
  .card--back { top: 465px; }

  .brand {
    display: flex; align-items: center; gap: 14px;
    white-space: nowrap;
  }
  .brand__mark {
    width: 54px; height: 54px; border-radius: 50%;
    border: 2px solid var(--ring); flex: none;
  }
  .brand__name {
    font-weight: 700; color: var(--ink); font-size: 20px; letter-spacing: 0.3px;
  }
  .card--front .brand {
    position: absolute; left: 50%; top: 50%;
    transform: translate(-50%, -50%);
  }

  .card--back .brand { position: absolute; left: 60px; top: 48px; }
  .card--back .brand__mark { width: 44px; height: 44px; }
  .card--back .brand__name { font-size: 17px; }

  .person { position: absolute; left: 60px; top: 130px; }
  .person__name { color: var(--accent); font-weight: 700; font-size: 20px; }
  .person__title {
    color: var(--ink-soft); font-size: 11px; letter-spacing: 0.6px;
    text-transform: uppercase; margin-top: 2px;
  }

  .contact {
    position: absolute; left: 60px; top: 200px;
    list-style: none; color: var(--ink); font-size: 16px; line-height: 27px;
    white-space: nowrap;
  }
  .contact__label { color: var(--accent); font-weight: 700; margin-right: 6px; }
  .contact__address { color: var(--ink-soft); }

  .decor { position: absolute; right: -120px; bottom: -110px; }
</style>
</head>
<body>
<main class="canvas">
  <section class="card card--front" aria-label="Card front">
    <div class="brand">
      <span class="brand__mark"></span>
      <span class="brand__name">Meridox Consulting Group LLC</span>
    </div>
  </section>

  <section class="card card--back" aria-label="Card back">
    <div class="brand">
      <span class="brand__mark"></span>
      <span class="brand__name">Meridox Consulting Group LLC</span>
    </div>
    <div class="person">
      <p class="person__name">Colin R. Vance</p>
      <p class="person__title">Chief Solutions Architect</p>
    </div>
    <ul class="contact">
      <li><span class="contact__label">O :</span>704.555.0142</li>
      <li><span class="contact__label">S :</span>704.555.0187</li>
      <li><span class="contact__label">e :</span>cvance@meridoxconsulting.com</li>
      <li class="contact__address">2715 Linden Park Dr., Suite 310 Charlotte, NC 28209</li>
    </ul>
    <svg class="decor" width="340" height="340" viewBox="0 0 340 340" aria-hidden="true">
      <circle cx="170" cy="170" r="160" fill="none" stroke="var(--ring-faint)" stroke-width="2"/>
    </svg>
  </section>
</main>
</body>
</html>
```